Cover design brief for the “Tides we can steer” collection

This collection aims to publish articles by several authors who are practitioners specializing in sociocracy, a participatory mode of governance that is highly innovative, and even quite subversive of the autocratic way in which companies and public institutions operate. However, this method has been widely and increasingly implemented since its initial development in the Netherlands in the 1970s and 80s. It is currently of particular interest to non-profit and cooperative organizations, citizen projects and intentional communities, as well as IT work teams (due to its proximity to the spirit of Agile methods).
The content is intellectually demanding. It won't be a matter of popularization for promotional purposes, but rather of subjects for reflection or in-depth analysis of practices, and feedback from field experience. Nor is it an academic journal.
The language used for these publications is French.
The target audience is French-speaking Europe and Canada.

Target Market(s)

The collection is aimed both at other practitioners of this method who want to develop their knowledge, and at people interested in the subjects of collective intelligence, cooperation and organization, in response to social, ecological and/or political concerns.

Industry/Entity Type

Training and consultancy

Font styles to use
Sans Serif

Requirements
Must have
• The name of the collection: Tides we can steer - Weaving the shared compass Each volume will mention the name of the collection as well as the theme of the volume. First one: Volume 1 - Crossing into layered views of teamwork. Selection criteria: - A singular, recurring visual identity for the volumes in the collection, highlighting its theme. - Appeal to potential readers; arouse curiosity. - Good readability of the text (title and subtitle, authors; presentation on back cover). - Simplicity of design variation for the cover of subsequent volumes (changing only the text). - Reasonable price in relation to a hoped-for circulation of between 100 and 300 copies per volume (the theme is linked to a niche that is still fairly narrow in the French-speaking world).
Nice to have
• Suggested graphic design directions If you have another direction to suggest with convincing arguments, we're open to your proposal. - The name of the collection, and in particular "Tides we can steer", will be visible at first glance. - The overall visual impression is one of movement and dynamism. - The style will be based on illustration work, such as sketchnotes. - The tone is playful and humorous. For example, it may mirror back to the potential reader the cultural clichés and social norms about power that make the theme "tides we can steer" a challenge to his or her imagination. As stated in the preface to Volume 1: "Most people are used to social environments where the choice is limited to suffering or fighting against powers that seek in a multitude of ways to put us at their service..."

```html
<!DOCTYPE html>
<html lang="en">
<head>
<meta charset="utf-8">
<title>Tides we can steer – Volume 1</title>
<link href="https://fonts.googleapis.com/css2?family=Bebas+Neue&family=Jost:wght@400;500&display=swap" rel="stylesheet">
<style>
  :root {
    --stage: #e9eef0;
    --paper: #ffffff;
    --ink: #141414;
    --title-top: #ef7a2a;
    --title-bottom: #cf3a22;
    --art-light: #fbe3cf;
    --art-mid: #f28a3a;
    --art-deep: #e0551f;
    --band: #151515;
    --band-text: #ffffff;
  }
  * { box-sizing: border-box; margin: 0; padding: 0; }
  html, body {
    width: 1200px;
    height: 800px;
    overflow: hidden;
    background: var(--stage);
  }
  .cover {
    position: absolute;
    left: 370px;
    top: 20px;
    width: 460px;
    height: 760px;
    background: var(--paper);
    display: flex;
    flex-direction: column;
    align-items: center;
    border-left: 6px double #e3e3e3;
    box-shadow: 0 6px 24px rgba(0,0,0,0.12);
  }
  .collection-line {
    margin-top: 28px;
    font-family: "Jost", sans-serif;
    font-weight: 400;
    font-size: 19px;
    letter-spacing: 1.2px;
    color: var(--ink);
    text-transform: uppercase;
  }
  .title {
    margin-top: 22px;
    font-family: "Bebas Neue", sans-serif;
    text-align: center;
    line-height: 0.9;
    background: linear-gradient(180deg, var(--title-top), var(--title-bottom));
    -webkit-background-clip: text;
    background-clip: text;
    color: transparent;
  }
  .title-line-1 { display: block; font-size: 104px; letter-spacing: 3px; }
  .title-line-2 { display: block; font-size: 80px; letter-spacing: 4px; margin-top: 8px; }
  .volume {
    margin-top: 22px;
    font-family: "Jost", sans-serif;
    font-weight: 500;
    font-size: 30px;
    color: var(--ink);
    text-transform: uppercase;
  }
  .volume-theme {
    margin-top: 10px;
    width: 400px;
    padding: 6px 0;
    border: 3px solid var(--ink);
    text-align: center;
    font-family: "Jost", sans-serif;
    font-size: 15px;
    letter-spacing: 1px;
    color: var(--ink);
    text-transform: uppercase;
  }
  .cover-art {
    margin-top: 14px;
    width: 360px;
    height: 320px;
    background:
      radial-gradient(ellipse 45% 60% at 50% 55%, var(--art-deep), transparent 70%),
      radial-gradient(ellipse 70% 75% at 50% 55%, var(--art-mid), transparent 75%),
      radial-gradient(ellipse 90% 90% at 50% 60%, var(--art-light), var(--paper) 80%);
  }
  .authors {
    margin-top: auto;
    width: 100%;
    height: 58px;
    background: var(--band);
    color: var(--band-text);
    display: flex;
    align-items: center;
    justify-content: center;
    font-family: "Jost", sans-serif;
    font-size: 24px;
    letter-spacing: 0.5px;
    text-transform: uppercase;
  }
</style>
</head>
<body>
  <article class="cover">
    <p class="collection-line">Weaving the shared compass</p>
    <h1 class="title">
      <span class="title-line-1">Tides we</span>
      <span class="title-line-2">can steer</span>
    </h1>
    <p class="volume">Volume 1 :</p>
    <p class="volume-theme">Crossing into layered views of teamwork</p>
    <div class="cover-art" role="img" aria-label="Sketch-style illustration: a circle of standing silhouettes gathered around a speaker, in front of rising orange brush strokes"></div>
    <p class="authors">Lucien Morvan, Daniel Ashford</p>
  </article>
</body>
</html>
```